Create a 2-sided postcard design (standard size) for Torvane Systems, a professional low-voltage and security integration company.
Side 1 – Front (Marketing Side)
Headline / Intro:
"Torvane Systems – Security, Connectivity, and Peace of Mind."
Brief Overview / Summary:
Torvane Systems provides complete security and technology integration solutions for commercial, industrial, and multifamily properties. From access control to fire systems, we specialize in delivering seamless, scalable, and reliable installations supported by professional service and ongoing care.
Services Breakdown:
Access Control – Cloud-based and enterprise access solutions to manage entry and permissions.
CCTV / Video Surveillance – Protect your property with high-definition cameras and remote monitoring.
Intrusion Alarm – Professional-grade systems to detect and deter unauthorized access.
Audio-Visual – From conference rooms to distributed audio and digital displays.
Fire Systems – Code-compliant alarm systems with 24/7 UL monitoring and life-safety support.
Structured Data Cabling – Low-voltage and fiber cabling for reliable network infrastructure.
Trusted By (Logos):
Melo, Plivantex, Grovelink, Carrow Investments, Bluff Hardware, Pinefold Games, Ledgerline Property Consultants, TRUEform
Technology partners:
Include logos of brands like Quelt, Otter Bank Networks, RMT , Lumen Sentrywell, Solmira, JFT, Blazecor
Contact Info:
📧 sales@torvanesystems.example
📞 760-555-0142
🌐 torvanesystems.example
🖼️ Side 2 – Back (Branding Side)
Primary Focus:
Large, centered Torvane Systems logo.
Subtext / Tagline (Optional):
“Your Security and Technology Partner.”
List of Services (Under Logo):
Access Control | CCTV | Intrusion Alarm | Audio-Visual | Fire | Data
🎨 Design Preferences:
Clean, modern, and professional layout.
Corporate tones (e.g., black and white, bold accents).
Use clean typography and icons for service areas.
Logo should be prominent on the back and represent the brand with strength and clarity.
Open to designer layout and creative interpretation as long as it stays on brand.

```html
<!DOCTYPE html>
<html lang="en">
<head>
<meta charset="utf-8">
<title>Torvane Systems – Postcard</title>
<link rel="stylesheet" href="https://fonts.googleapis.com/css2?family=Questrial&display=swap">
<style>
  :root {
    --page: #e4e4e4;
    --card: #07131a;
    --title: #c3ccd3;
    --text: #eef1f3;
    --muted: #d6dce0;
    --rule: #3a464d;
    --icon: #c9d0d5;
  }
  * { box-sizing: border-box; margin: 0; padding: 0; }
  html, body { width: 929px; height: 1200px; overflow: hidden; background: var(--page); }
  body { position: relative; font-family: "Questrial", sans-serif; color: var(--text); }

  .card { position: absolute; left: 94px; width: 741px; height: 494px; background: var(--card); overflow: hidden; }
  .card--front { top: 92px; }
  .card--back { top: 613px; }
  .abs { position: absolute; }
  .center { left: 0; right: 0; text-align: center; }

  .motif { position: absolute; border-radius: 50%;
    background: radial-gradient(closest-side, rgba(160,175,185,0.10), rgba(160,175,185,0.03) 70%, transparent); }
  .wave-texture { position: absolute; left: 0; right: 0; bottom: 0; height: 300px;
    background: radial-gradient(ellipse 60% 70% at 20% 75%, rgba(190,200,210,0.12), transparent 70%),
                radial-gradient(ellipse 60% 60% at 80% 55%, rgba(190,200,210,0.10), transparent 70%); }

  .headline { top: 56px; font-size: 49px; color: var(--title); line-height: 1; letter-spacing: -0.5px; }
  .subhead { top: 110px; font-size: 23px; line-height: 1; }
  .intro { top: 147px; font-size: 12.2px; line-height: 16px; }

  .rule { position: absolute; height: 1px; background: var(--rule); }
  .vrule { position: absolute; width: 1px; background: var(--rule); }

  .services-label { left: 59px; top: 265px; font-size: 23px; line-height: 1; }
  .service { position: absolute; display: flex; gap: 8px; align-items: flex-start; }
  .service svg { width: 15px; height: 15px; margin-top: 2px; flex: none; stroke: var(--icon); fill: none; stroke-width: 1.2; }
  .service__name { font-size: 12px; line-height: 14px; }
  .service__desc { font-size: 11px; line-height: 14px; color: var(--muted); }

  .info-col { position: absolute; top: 378px; width: 215px; text-align: center; }
  .info-col h3 { font-weight: 400; font-size: 20px; line-height: 24px; margin-bottom: 9px; }
  .info-col p { font-size: 10.5px; line-height: 17.5px; color: var(--muted); }
  .contact-line { display: flex; justify-content: center; align-items: center; gap: 4px; font-size: 10.5px; line-height: 17.5px; }
  .contact-line--phone { font-size: 13px; }
  .contact-line svg { width: 10px; height: 10px; fill: var(--muted); }

  .wordmark { top: 138px; display: flex; justify-content: center; align-items: center; gap: 16px; }
  .wordmark__square { width: 56px; height: 56px; border: 4px solid #ffffff; }
  .wordmark__name { font-size: 52px; line-height: 1; color: #ffffff; letter-spacing: 1px; }
  .service-list { top: 253px; font-size: 20px; line-height: 25px; }
  .tagline { top: 340px; font-size: 22px; line-height: 1; }
</style>
</head>
<body>

<section class="card card--front">
  <div class="motif" style="left:20px;top:-10px;width:200px;height:230px;" role="img" aria-label="Faint geometric motif of outlined squares, rings and an arrow"></div>
  <div class="motif" style="left:580px;top:250px;width:190px;height:230px;" role="img" aria-label="Faint geometric motif of outlined squares, rings and an arrow"></div>

  <h1 class="abs center headline" style="font-weight:400;">Torvane Systems</h1>
  <h2 class="abs center subhead" style="font-weight:400;">Security, Connectivity, and Peace of Mind</h2>
  <p class="abs center intro">Complete security and technology integration for commercial, industrial, and<br>multifamily properties. Reliable installations with professional service and support.</p>

  <div class="rule" style="left:23px;width:695px;top:202px;"></div>

  <h3 class="abs services-label" style="font-weight:400;">Services</h3>

  <div class="service" style="left:186px;top:224px;">
    <svg viewBox="0 0 16 16"><rect x="3" y="7" width="10" height="8" rx="1"/><path d="M5 7V5a3 3 0 0 1 6 0v2"/></svg>
    <div><div class="service__name">Access Control</div><div class="service__desc">Cloud &amp; enterprise entry systems</div></div>
  </div>
  <div class="service" style="left:186px;top:260px;">
    <svg viewBox="0 0 16 16"><rect x="1" y="4" width="10" height="6" rx="1"/><path d="M11 6l4-2v6l-4-2M4 10v4h4"/></svg>
    <div><div class="service__name">CCTV / Video Surveillance</div><div class="service__desc">HD cameras &amp; remote monitoring</div></div>
  </div>
  <div class="service" style="left:186px;top:296px;">
    <svg viewBox="0 0 16 16"><path d="M8 2l7 12H1z"/><path d="M8 6v4M8 12v.5"/></svg>
    <div><div class="service__name">Intrusion Alarm</div><div class="service__desc">Detect &amp; deter unauthorized access</div></div>
  </div>

  <div class="vrule" style="left:405px;top:225px;height:100px;"></div>

  <div class="service" style="left:425px;top:224px;">
    <svg viewBox="0 0 16 16"><rect x="1" y="2" width="11" height="9"/><path d="M5 5l3 1.5L5 8z"/><path d="M12 9v3a2 2 0 0 0 3 0"/></svg>
    <div><div class="service__name">Audio-Visual</div><div class="service__desc">Meeting rooms, digital displays, distributed audio</div></div>
  </div>
  <div class="service" style="left:425px;top:260px;">
    <svg viewBox="0 0 16 16"><ellipse cx="8" cy="6" rx="7" ry="3"/><path d="M2 7v2c0 2 12 2 12 0V7M6 11l2 2 2-2"/></svg>
    <div><div class="service__name">Fire Systems</div><div class="service__desc">Code-compliant alarms, 24/7 UL monitoring</div></div>
  </div>
  <div class="service" style="left:425px;top:296px;">
    <svg viewBox="0 0 16 16"><path d="M4 1v4M12 1v4M4 5v5a4 4 0 0 0 8 0V5"/></svg>
    <div><div class="service__name">Structured Data Cabling</div><div class="service__desc">Low-voltage &amp; fiber networks</div></div>
  </div>

  <div class="rule" style="left:23px;width:695px;top:345px;"></div>

  <div class="info-col" style="left:36px;">
    <h3>Trusted By</h3>
    <p>Melo | Plivantex | Grovelink | Carrow Investments | Bluff Hardware | TRUEform | Ledgerline Property Consultants</p>
  </div>
  <div class="vrule" style="left:265px;top:383px;height:82px;"></div>
  <div class="info-col" style="left:272px;">
    <h3>Technology Partners</h3>
    <p>Quelt | Otter Bank Networks | RMT | Lumen Sentrywell | Solmira | JFT | Blazecor</p>
  </div>
  <div class="vrule" style="left:496px;top:383px;height:82px;"></div>
  <div class="info-col" style="left:483px;">
    <h3>Contact</h3>
    <div class="contact-line contact-line--phone">
      <svg viewBox="0 0 16 16"><path d="M3 1l3 1 1 3-2 2a9 9 0 0 0 4 4l2-2 3 1 1 3-2 2C7 15 1 9 1 3z"/></svg>760-555-0142
    </div>
    <div class="contact-line">
      <svg viewBox="0 0 16 16"><path d="M1 3h14v10H1z M1 3l7 6 7-6" /></svg>sales@torvanesystems.example
    </div>
    <div class="contact-line">
      <svg viewBox="0 0 16 16"><path d="M3 1l10 7-4 1 3 5-2 1-3-5-3 3z"/></svg>torvanesystems.example
    </div>
  </div>
</section>

<section class="card card--back">
  <div class="wave-texture" role="img" aria-label="Soft dotted sound-wave texture across the lower half"></div>
  <div class="motif" style="left:5px;top:5px;width:210px;height:230px;" role="img" aria-label="Faint geometric motif of outlined squares, rings and an arrow"></div>

  <div class="abs center wordmark">
    <div class="wordmark__square"></div>
    <div class="wordmark__name">Torvane Systems</div>
  </div>

  <p class="abs center service-list">Access Control | CCTV | Intrusion<br>Alarm | Audio-Visual | Fire | Data</p>
  <div class="rule" style="left:123px;width:494px;top:321px;"></div>
  <p class="abs center tagline">Your Security and Technology Partner.</p>
</section>

</body>
</html>
```